Brisk Nook needs a packaging design

Hello!

I need an eye-catching package design for Brisk Nook mobile accessories. The products inside the box package include a bluetooth speaker and a power bank.

This is under our brandname called Brisk Nook. The text should be in the picture, no matter how the design looks.

I have attached pictures of the products. If you think that there will not be well with the images it is ok. Then these texts be included:
Bluetooth Speaker
Power Bank

This is our slogan:
Music + Power. It's your imagination that sets the limits!

The image will be printed on a carton pack containing with four color printing. Customising the picture for the type of print.

Should be in 300 DPI High resolution.

Please check the attached pictures where your design will be printed.
Also, I attached design inspiration images for reference. Feel free to do something similar like that.

For the size and dimensions please refer to this attachment:

So remember, the important thing is the design. Do your absolute best!
Updates

Reason: Hello everyone! I would like to see a design without the images of the accessories. Only text. I also dont want the text "Its you imagination that sets...". Thank you!

Target Market(s)

Mobile accessories

Industry/Entity Type

Electronics

Requirements
Must have
• This text:
• Brisk Nook
Nice to have
• Music + Power.

```html
<!DOCTYPE html>
<html lang="en">
<head>
<meta charset="utf-8">
<title>Brisk Nook – Package Front</title>
<link rel="stylesheet" href="https://fonts.googleapis.com/css2?family=Exo+2:wght@500;600;800&display=swap">
<style>
  :root {
    --canvas-bg: #e9e7e4;
    --panel-top: #1a1638;
    --panel-mid: #100d24;
    --panel-bottom: #07060f;
    --brand-red: #e01a22;
    --text-light: #d9d9e3;
    --wave-violet: #7b3fd6;
    --wave-blue: #2f6fd8;
    --wave-red: #e0334a;
    --wave-amber: #f0a13a;
  }
  * { margin: 0; padding: 0; box-sizing: border-box; }
  html, body {
    width: 1200px;
    height: 800px;
    overflow: hidden;
    background: var(--canvas-bg);
    font-family: "Exo 2", "Segoe UI", sans-serif;
  }
  .canvas {
    position: relative;
    width: 1200px;
    height: 800px;
    display: flex;
    align-items: center;
    justify-content: center;
  }
  .package-front {
    position: relative;
    width: 640px;
    height: 680px;
    background: radial-gradient(ellipse at 40% 30%, var(--panel-top) 0%, var(--panel-mid) 50%, var(--panel-bottom) 100%);
    box-shadow: 0 18px 40px rgba(0, 0, 0, 0.25);
    overflow: hidden;
  }
  .brand-name {
    position: absolute;
    top: 62px;
    left: 52px;
    font-weight: 800;
    font-size: 72px;
    letter-spacing: 2px;
    text-transform: uppercase;
    color: var(--brand-red);
    line-height: 1;
    white-space: nowrap;
  }
  .slogan {
    position: absolute;
    top: 152px;
    left: 56px;
    font-weight: 600;
    font-size: 19px;
    color: var(--text-light);
  }
  .light-waves {
    position: absolute;
    top: 250px;
    left: 0;
    width: 100%;
    height: 260px;
    background:
      radial-gradient(ellipse 55% 35% at 30% 45%, rgba(123, 63, 214, 0.55), transparent 70%),
      radial-gradient(ellipse 45% 30% at 60% 50%, rgba(47, 111, 216, 0.45), transparent 70%),
      radial-gradient(ellipse 40% 28% at 85% 55%, rgba(224, 51, 74, 0.55), transparent 70%),
      radial-gradient(ellipse 18% 18% at 97% 55%, rgba(240, 161, 58, 0.5), transparent 70%);
  }
  .product-list,
  .product-line {
    position: absolute;
    bottom: 44px;
    font-weight: 600;
    font-size: 17px;
    line-height: 1.25;
    text-transform: uppercase;
    color: var(--text-light);
    list-style: none;
  }
  .product-list {
    left: 56px;
    text-align: left;
  }
  .product-line {
    right: 48px;
    text-align: center;
  }
</style>
</head>
<body>
  <main class="canvas">
    <section class="package-front">
      <h1 class="brand-name">Brisk Nook</h1>
      <p class="slogan">Music + Power.</p>
      <div class="light-waves" role="img" aria-label="Flowing ribbons of violet, blue and red light waves crossing the box"></div>
      <ul class="product-list">
        <li>Bluetooth Speaker</li>
        <li>Power Bank</li>
      </ul>
      <p class="product-line">All mobile<br>accesories</p>
    </section>
  </main>
</body>
</html>
```